Postcard Design Harlow Bend D to D

Residential Real Estate, we want to implement a mail campaign in an specific geographic area.We want to include Market information on the area and statistics of the real estate market.This piece is going to be deliver via mail service door to door.

Target Market(s)

Home owners that might be interested in selling their houses

Industry/Entity Type

Real Estate

Font styles to use
Sans Serif

Colors
ec1f27
f78f20

Requirements
Must have
• Attractive look
• Include the information that we just sent to you
• Clear graphics and tables
• Must include clear information about our group

```html
<!DOCTYPE html>
<html lang="en">
<head>
<meta charset="utf-8">
<title>Harlow Bend Market Update</title>
<link rel="stylesheet" href="https://fonts.googleapis.com/css2?family=Roboto:wght@400;700;900&family=Source+Sans+3:ital,wght@0,400;0,600;1,600&display=swap">
<style>
:root{
  --red:#c1202a;
  --brand-red:#ec1f27;
  --orange:#f78f20;
  --text:#222;
  --grey:#555;
  --white:#fff;
}
*{margin:0;padding:0;box-sizing:border-box}
html,body{width:1200px;height:926px;overflow:hidden;background:var(--white)}
body{position:relative;font-family:"Roboto",Arial,sans-serif;color:var(--text)}
.header{position:absolute;left:0;top:0;width:1200px;height:157px;background:var(--red);color:var(--white)}
.header-band{position:absolute;left:0;top:157px;width:1200px;height:14px;background:var(--orange)}
.headline{position:absolute;left:48px;top:14px;font-weight:900;font-size:36px;letter-spacing:2.4px;white-space:nowrap}
.headline em{font-style:italic}
.intro{position:absolute;left:48px;top:66px;font-family:"Source Sans 3",sans-serif;font-size:23.5px;line-height:31px;white-space:nowrap}
.intro em{color:var(--orange);font-weight:600}
.section-title{position:absolute;background:var(--red);color:var(--white);font-size:24px;display:flex;align-items:center;justify-content:center;letter-spacing:.3px}
.axis-note{position:absolute;font-size:16px}
.caption{position:absolute;font-size:15.5px}
table.market{position:absolute;border-collapse:collapse;table-layout:fixed;font-size:15px;text-align:center}
.market td,.market th{border:2px solid var(--orange);padding:0}
.market thead th{background:var(--orange);color:var(--white);font-weight:400;font-size:12.5px}
.market thead th.price,.market thead th.total{font-size:17.5px}
.market tbody td:first-child{font-size:16.5px}
.market tbody td.total{font-weight:700;font-size:17px}
.market tfoot td{background:var(--orange);color:var(--white);font-weight:700;font-size:15px}
.market tfoot td:first-child{font-size:18px}
#active{left:43px;top:281px;width:531px}
#active thead tr{height:34px}
#active tbody tr{height:30.3px}
#active tfoot tr{height:25px}
#sold{left:43px;top:681px;width:582px}
#sold thead tr{height:33px}
#sold tbody tr{height:24px}
#sold tfoot tr{height:26px}
.chart{position:absolute;left:690px;top:390px}
.chart text{font-family:"Roboto",Arial,sans-serif;fill:var(--text)}
.footnote{position:absolute;left:724px;top:665px;font-size:14px}
.brand{position:absolute;left:790px;top:816px;font-family:"Source Sans 3",sans-serif;font-weight:400;font-size:42px;color:#4a4a4a;letter-spacing:-.5px;white-space:nowrap}
</style>
</head>
<body>
<header class="header">
  <h1 class="headline">Updated information to help you make a <em>smart decision!</em></h1>
  <p class="intro">If you are planning <em>to sell or buy your home</em> let us provide you with updated and accurate information.<br>Let us help to <em>maximize your profit</em> in the most effective way, following a secure and smooth journey.</p>
</header>
<div class="header-band"></div>

<div class="section-title" style="left:42px;top:203px;width:532px;height:50px">Active on the Market</div>
<div class="axis-note" style="left:155px;top:259px">Days on Market</div>
<table class="market" id="active">
  <colgroup><col style="width:111px"><col span="7" style="width:52px"><col style="width:56px"></colgroup>
  <thead><tr><th class="price">Sold Price</th><th>0-29</th><th>30-59</th><th>60-89</th><th>90-119</th><th>120-149</th><th>150-179</th><th>180-209</th><th class="total">Total</th></tr></thead>
  <tbody>
    <tr><td>$150 -$199</td><td>1</td><td></td><td>1</td><td>1</td><td></td><td></td><td></td><td class="total">3</td></tr>
    <tr><td>$200 -$249</td><td>2</td><td></td><td></td><td>1</td><td>1</td><td></td><td></td><td class="total">4</td></tr>
    <tr><td>$250 - $299</td><td>1</td><td>3</td><td></td><td>2</td><td></td><td></td><td></td><td class="total">6</td></tr>
    <tr><td>$300 -$ 349</td><td>5</td><td>2</td><td></td><td></td><td></td><td></td><td>2</td><td class="total">9</td></tr>
    <tr><td>$350 - $399</td><td>2</td><td></td><td></td><td>1</td><td></td><td>1</td><td></td><td class="total">4</td></tr>
    <tr><td>$400 - $449</td><td>1</td><td></td><td></td><td></td><td></td><td></td><td></td><td class="total">1</td></tr>
    <tr><td>$450 - $499</td><td></td><td></td><td></td><td>1</td><td></td><td></td><td></td><td class="total">1</td></tr>
  </tbody>
  <tfoot><tr><td>Total</td><td>12</td><td>5</td><td>1</td><td>6</td><td>1</td><td>1</td><td>2</td><td>28</td></tr></tfoot>
</table>
<div class="caption" style="left:43px;top:552px">House Price Sold by range of $50K</div>

<div class="section-title" style="left:42px;top:599px;width:583px;height:51px">Sold Properties (Past 6 Months)</div>
<div class="axis-note" style="left:155px;top:657px">Days on Market</div>
<table class="market" id="sold">
  <colgroup><col style="width:111px"><col span="8" style="width:52px"><col style="width:55px"></colgroup>
  <thead><tr><th class="price">Sold Price</th><th>0-29</th><th>30-59</th><th>60-89</th><th>90-119</th><th>120-149</th><th>150-179</th><th>180-209</th><th>210-239</th><th class="total">Total</th></tr></thead>
  <tbody>
    <tr><td>$170 -$219</td><td>23</td><td>3</td><td>3</td><td>1</td><td>2</td><td>1</td><td></td><td></td><td class="total">33</td></tr>
    <tr><td>$220 -$ 269</td><td>11</td><td>5</td><td>5</td><td>1</td><td></td><td></td><td></td><td></td><td class="total">22</td></tr>
    <tr><td>$270 - $319</td><td>10</td><td>5</td><td>5</td><td>1</td><td></td><td></td><td></td><td></td><td class="total">21</td></tr>
    <tr><td>$320 -$369</td><td>9</td><td></td><td></td><td></td><td></td><td>1</td><td>1</td><td>2</td><td class="total">13</td></tr>
    <tr><td>$370-$ 420</td><td>3</td><td>3</td><td>1</td><td></td><td>1</td><td></td><td></td><td></td><td class="total">8</td></tr>
  </tbody>
  <tfoot><tr><td>Total</td><td>56</td><td>16</td><td>14</td><td>3</td><td>3</td><td>2</td><td>1</td><td>2</td><td>97</td></tr></tfoot>
</table>
<div class="caption" style="left:43px;top:865px">House Price Sold by range of $50K</div>

<div class="section-title" style="left:690px;top:305px;width:460px;height:50px">The Historic Price per sqf. 2003 - 2014</div>
<div class="axis-note" style="left:691px;top:372px;font-size:14.5px">$ Price per sqf.</div>
<svg class="chart" width="470" height="270" viewBox="0 0 470 270" role="img" aria-label="Bar chart of price per square foot, 2003 to 2014">
  <g stroke="#777" stroke-width="1">
    <line x1="32" y1="17" x2="458" y2="17"/>
    <line x1="32" y1="73.75" x2="458" y2="73.75"/>
    <line x1="32" y1="130.5" x2="458" y2="130.5"/>
    <line x1="32" y1="187.25" x2="458" y2="187.25"/>
    <line x1="32" y1="244" x2="458" y2="244"/>
  </g>
  <g font-size="13" text-anchor="end">
    <text x="22" y="22">100</text><text x="22" y="79">90</text><text x="22" y="135">80</text><text x="22" y="192">70</text><text x="22" y="248">60</text>
  </g>
  <text x="215" y="49" font-size="19" text-anchor="middle">Trend</text>
  <g fill="var(--red)">
    <rect x="35" y="190" width="22" height="54"/>
    <rect x="71" y="217" width="22" height="27"/>
    <rect x="107" y="187" width="22" height="57"/>
    <rect x="142" y="155" width="22" height="89"/>
    <rect x="178" y="107" width="22" height="137"/>
    <rect x="214" y="143" width="22" height="101"/>
    <rect x="250" y="113" width="22" height="131"/>
    <rect x="285" y="110" width="22" height="134"/>
    <rect x="321" y="113" width="22" height="131"/>
    <rect x="357" y="99" width="22" height="145"/>
    <rect x="392" y="73.75" width="22" height="170.25"/>
    <rect x="428" y="35" width="22" height="209"/>
  </g>
  <g font-size="13" text-anchor="middle">
    <text x="46" y="262">2003</text><text x="82" y="262">2004</text><text x="118" y="262">2005</text><text x="153" y="262">2006</text><text x="189" y="262">2007</text><text x="225" y="262">2008</text><text x="261" y="262">2009</text><text x="296" y="262">2010</text><text x="332" y="262">2011</text><text x="368" y="262">2012</text><text x="403" y="262">2013</text><text x="439" y="262">2014</text>
  </g>
</svg>
<div class="footnote">*Data from Harlow Bend Association of Realtors</div>

<div class="brand">The Ortega Group</div>
</body>
</html>
```